Fertility Book Cover

This is a book about infertility, treatment options and solutions. The book title is "No caminho do amanhecer". The book is in portuguese, but I believe that won't be a problem to design the cover. I need front and back covers design.
The author name, that should be in book is "Dra. Beatriz Morano Vasconti Telhado".

Letter case could be "No Caminho do Amanhecer"

This is the cover I created, but I don't like it: http://www.docuvelo.com/doc/583190462/27390518-cover

8.5" x 11"

Target Market(s)

Woman and Couples that desire kids and have problem about fertility

Colors
b768aa
e34196
6b449a

Requirements
Nice to have
• a link to our domain: www.ninhoclaro.org (not essential)
More happy images than sad woman...

```html
<!DOCTYPE html>
<html lang="pt">
<head>
<meta charset="utf-8">
<title>No caminho do amanhecer</title>
<link rel="stylesheet" href="https://fonts.googleapis.com/css2?family=Dosis:wght@300;400&display=swap">
<style>
  :root {
    --ink-plum: #5b3a5a;
    --cream: #e3e0ce;
    --cream-warm: #e4dccb;
    --skin-light: #ecd6c6;
    --skin-warm: #e5c4b0;
    --skin-deep: #d9b19d;
  }
  html, body {
    margin: 0;
    padding: 0;
    width: 806px;
    height: 1200px;
    overflow: hidden;
    background: var(--cream);
  }
  .book-cover {
    position: relative;
    width: 806px;
    height: 1200px;
    overflow: hidden;
  }
  .cover-photo {
    position: absolute;
    inset: 0;
    background:
      radial-gradient(ellipse 320px 520px at 700px 330px, var(--skin-light) 0%, rgba(236,214,198,0) 100%),
      radial-gradient(ellipse 260px 360px at 700px 820px, #f3efe4 0%, rgba(243,239,228,0) 100%),
      linear-gradient(to bottom, rgba(0,0,0,0) 70%, var(--skin-deep) 100%),
      linear-gradient(to right, var(--cream) 0%, var(--cream-warm) 45%, var(--skin-warm) 75%, var(--skin-light) 100%);
  }
  .book-title {
    position: absolute;
    left: 88px;
    top: 178px;
    margin: 0;
    font-family: "Dosis", sans-serif;
    font-weight: 300;
    font-size: 150px;
    line-height: 185px;
    color: var(--ink-plum);
    letter-spacing: -1px;
  }
  .book-title span { display: block; }
  .author-name {
    position: absolute;
    left: 88px;
    top: 1108px;
    margin: 0;
    font-family: "Dosis", sans-serif;
    font-weight: 400;
    font-size: 42px;
    line-height: 50px;
    color: var(--ink-plum);
    white-space: nowrap;
  }
</style>
</head>
<body>
  <main class="book-cover">
    <div class="cover-photo" role="img" aria-label="Soft-focus photograph of a woman with closed eyes holding a white flower near her face, on a pale cream background"></div>
    <h1 class="book-title">
      <span>No</span>
      <span>caminho</span>
      <span>do</span>
      <span>amanhecer</span>
    </h1>
    <p class="author-name">Dra. Beatriz Morano Vasconti Telhado</p>
  </main>
</body>
</html>
```